GLOW NOW 14 DAY Challange

looking to make a poster that needs to be 36" wide x24"tall design graphic . Check out the added file as it is a rough draft of the material I would like it to say.

Phone number 555-014-2736 www.rbchiropractic..com

Adults aged 25-45 high income adults needing to make changes in dies and lose weight

```html
<!DOCTYPE html>
<html lang="en">
<head>
<meta charset="utf-8">
<title>Glow Now 14 Day Challenge Poster</title>
<link href="https://fonts.googleapis.com/css2?family=Lexend:wght@400;500;600;700&display=swap" rel="stylesheet">
<style>
  :root{
    --red:#e8101a;
    --navy:#33338f;
    --ink:#111111;
    --white:#ffffff;
    --backdrop:#e9e8e6;
    --photo-top:#f1ede9;
    --photo-mid:#c9b3a3;
    --photo-low:#6f88a6;
  }
  html,body{margin:0;padding:0;width:1200px;height:1148px;overflow:hidden;background:var(--backdrop);}
  body{position:relative;font-family:"Lexend",sans-serif;}
  .poster{position:absolute;left:60px;top:214px;width:1080px;height:720px;background:var(--white);box-shadow:0 6px 24px rgba(0,0,0,.12);overflow:hidden;}
  .brand{position:absolute;left:50px;top:34px;display:flex;align-items:center;gap:12px;color:var(--navy);font-weight:700;font-size:32px;letter-spacing:1px;line-height:1;}
  .brand-mark{width:30px;height:30px;border-radius:50%;background:var(--navy);}
  .headline{position:absolute;left:48px;top:96px;margin:0;line-height:1;font-weight:700;}
  .headline .line-a{display:block;color:var(--red);font-size:66px;letter-spacing:-1px;}
  .headline .line-b{display:block;color:var(--navy);font-size:90px;letter-spacing:-4px;margin-top:2px;}
  .headline .line-c{display:block;color:var(--red);font-size:50px;margin-top:4px;}
  .photo{position:absolute;left:760px;top:0;width:320px;height:666px;background:linear-gradient(180deg,var(--photo-top) 0%,var(--photo-mid) 45%,var(--photo-low) 80%,var(--photo-low) 100%);}
  .steps{position:absolute;left:50px;top:346px;margin:0;padding:0;list-style:none;}
  .steps li{display:flex;align-items:center;gap:6px;height:42px;font-size:18px;font-weight:500;color:var(--ink);white-space:nowrap;}
  .steps svg{width:32px;height:30px;flex:none;}
  .concerns{position:absolute;left:460px;top:356px;margin:0;padding:0;list-style:none;}
  .concerns li{display:flex;align-items:center;gap:14px;height:40px;font-size:17px;color:var(--red);white-space:nowrap;}
  .concerns svg{width:13px;height:12px;flex:none;}
  .cta{position:absolute;left:460px;top:540px;margin:0;color:var(--red);font-weight:600;font-size:18px;white-space:nowrap;}
  .contact-band{position:absolute;left:0;right:0;bottom:0;height:54px;background:var(--red);display:flex;align-items:center;padding:0 0 0 50px;gap:16px;color:var(--white);font-size:24px;font-weight:500;}
  .social{margin-left:auto;margin-right:24px;display:flex;gap:6px;}
  .social span{width:30px;height:30px;background:var(--white);border-radius:3px;}
</style>
</head>
<body>
  <main class="poster">
    <div class="brand"><span class="brand-mark"></span>RIDGEBACK CHIROPRACTIC</div>

    <h1 class="headline">
      <span class="line-a">GLOW NOW</span>
      <span class="line-b">14 DAY</span>
      <span class="line-c">CHALLENGE</span>
    </h1>

    <div class="photo" role="img" aria-label="Photo of a smiling woman measuring her waist with a tape measure"></div>

    <ul class="steps">
      <li><svg viewBox="0 0 36 34"><path d="M18 32 C6 22 1 16 1 10 A8.5 8.5 0 0 1 18 6 A8.5 8.5 0 0 1 35 10 C35 16 30 22 18 32Z" fill="var(--red)"/></svg>:LIVER DETOX PURIFICATION</li>
      <li><svg viewBox="0 0 36 34"><path d="M18 32 C6 22 1 16 1 10 A8.5 8.5 0 0 1 18 6 A8.5 8.5 0 0 1 35 10 C35 16 30 22 18 32Z" fill="var(--red)"/></svg>:OMEGA 3 SUPPLEMENTS</li>
      <li><svg viewBox="0 0 36 34"><path d="M18 32 C6 22 1 16 1 10 A8.5 8.5 0 0 1 18 6 A8.5 8.5 0 0 1 35 10 C35 16 30 22 18 32Z" fill="var(--red)"/></svg>:VIT D SUPPLEMENTS</li>
      <li><svg viewBox="0 0 36 34"><path d="M18 32 C6 22 1 16 1 10 A8.5 8.5 0 0 1 18 6 A8.5 8.5 0 0 1 35 10 C35 16 30 22 18 32Z" fill="var(--red)"/></svg>:EAT FRUITS AND VEGGIES</li>
      <li><svg viewBox="0 0 36 34"><path d="M18 32 C6 22 1 16 1 10 A8.5 8.5 0 0 1 18 6 A8.5 8.5 0 0 1 35 10 C35 16 30 22 18 32Z" fill="var(--red)"/></svg>:KEFIR HOMEMADE PROBIOTIC</li>
      <li><svg viewBox="0 0 36 34"><path d="M18 32 C6 22 1 16 1 10 A8.5 8.5 0 0 1 18 6 A8.5 8.5 0 0 1 35 10 C35 16 30 22 18 32Z" fill="var(--red)"/></svg>:CHIROPRACTIC ADJUSTMENTS</li>
    </ul>

    <ul class="concerns">
      <li><svg viewBox="0 0 36 34"><path d="M18 32 C6 22 1 16 1 10 A8.5 8.5 0 0 1 18 6 A8.5 8.5 0 0 1 35 10 C35 16 30 22 18 32Z" fill="var(--navy)"/></svg>Do you have Allergies</li>
      <li><svg viewBox="0 0 36 34"><path d="M18 32 C6 22 1 16 1 10 A8.5 8.5 0 0 1 18 6 A8.5 8.5 0 0 1 35 10 C35 16 30 22 18 32Z" fill="var(--navy)"/></svg>Always feeling tired</li>
      <li><svg viewBox="0 0 36 34"><path d="M18 32 C6 22 1 16 1 10 A8.5 8.5 0 0 1 18 6 A8.5 8.5 0 0 1 35 10 C35 16 30 22 18 32Z" fill="var(--navy)"/></svg>ACHES and PAINS</li>
      <li><svg viewBox="0 0 36 34"><path d="M18 32 C6 22 1 16 1 10 A8.5 8.5 0 0 1 18 6 A8.5 8.5 0 0 1 35 10 C35 16 30 22 18 32Z" fill="var(--navy)"/></svg>Carry lots of water weight</li>
    </ul>

    <p class="cta">CONTACT TODAY FOR DETAILS</p>

    <footer class="contact-band">
      <span class="phone">555-014-2736</span>
      <span class="web">www.rbchiropractic..com</span>
      <div class="social"><span></span><span></span></div>
    </footer>
  </main>
</body>
</html>
```